Kickmark Figures Service

We have a football stats service that we feel would benefit from some design input. In particular we would like the designer to look at three pages. We will then transfer this style across the rest of the site.

We are looking for designs for three pages. Links to the existing pages we would like reworked are:

Player:
http://demostats.kickmark-example.com/Player.asp?lang=&coid=4&teid=220&plid=197404

Team Stats:
http://demostats.kickmark-example.com/Team_Stats.asp?lang=&coid=4&teid=218

League Table:
http://demostats.kickmark-example.com/Comp_Table.asp?lang=&coid=4

We require the page structure to remain as is with the main country/competition selector on the left and the content on the right.

The colour palette, fonts, content separators etc are all in your hands. We will use this version as a sales tool for our services. In many cases this will be restyled to match a specific clients requirements.

We are happy for this to be done in HTML/CSS or as a layered image file.

Target Market(s)

These stats pages are for use on newspaper and bookmaker websites.

Industry/Entity Type

Sales

Requirements
Nice to have
• A nice colour palette for graphs and charts is important.

```html
<!DOCTYPE html>
<html lang="en">
<head>
<meta charset="utf-8">
<title>Kickmark Data Systems – Player</title>
<link href="https://fonts.googleapis.com/css2?family=Oxygen:wght@300;400;700&family=Arimo:wght@400;700&display=swap" rel="stylesheet">
<style>
:root{
  --green:#5b9232;
  --green-dark:#4b7f26;
  --green-line:#6ea244;
  --orange:#ff7a00;
  --orange-light:#ffa000;
  --purple:#7a35c0;
  --purple-text:#8a3fc0;
  --text:#333;
  --muted:#555;
  --line:#e2e2e2;
  --panel-head:#f3f3f3;
  --footer:#eeeeee;
}
*{box-sizing:border-box;margin:0;padding:0}
html,body{width:1200px;height:1098px;overflow:hidden;background:#fff}
body{position:relative;font-family:"Oxygen",sans-serif;color:var(--text);font-size:13px}
.abs{position:absolute}
.header{left:0;top:0;width:1200px;height:120px;background:linear-gradient(#fff,#f4f4f4);border-bottom:1px solid #ddd}
.brand-mark{left:127px;top:31px;width:62px;height:62px;background:var(--green)}
.brand-name{left:195px;top:50px;font-family:"Arimo",sans-serif;font-weight:700;font-size:23px;color:#222}
.brand-tag{left:195px;top:79px;font-family:"Arimo",sans-serif;font-size:11px;color:#222}
.radio{top:40px;font-size:13px;color:#333;display:flex;align-items:center;gap:5px}
.radio i{display:inline-block;width:13px;height:13px;border:1px solid #bbb;border-radius:50%;background:#fff}
.search{left:568px;top:62px;width:292px;height:31px;border:1px solid #ccc;background:#fff;font-size:11px;color:#999;padding:9px 14px}
.search-btn{left:827px;top:62px;width:33px;height:31px;background:var(--orange)}
.date{right:130px;top:48px;font-size:14px;color:#222;text-align:right}
.today{right:130px;top:69px;font-size:16px;color:var(--orange);text-align:right}

.sidebar{left:126px;top:159px;width:215px;height:441px;background:var(--green);border-radius:3px;overflow:hidden}
.side-head{height:43px;background:var(--green-dark);color:#fff;font-size:17px;padding:13px 0 0 27px}
.side-item{height:28px;border-bottom:1px solid var(--green-line);color:#fff;font-size:13.5px;display:flex;align-items:center;padding-left:30px;gap:11px}
.side-item:last-child{border-bottom:none}
.side-item.plain{height:32.5px;padding-left:29px;font-weight:300;font-size:14px}
.flag{width:21px;height:13px;display:block}

.card{border:1px solid #ddd;border-radius:3px;background:#fff}
.profile{left:361px;top:158px;width:713px;height:201px}
.photo{left:20px;top:18px;width:160px;height:156px;border-radius:2px;background:linear-gradient(135deg,#5e5a56,#2d2a28)}
.p-name{left:201px;top:22px;font-size:24px;color:var(--orange)}
.p-club{left:201px;top:56px;font-size:17px;color:var(--green);display:flex;align-items:center;gap:10px}
.facts{font-size:12.8px;color:var(--muted)}
.facts b{font-weight:400;color:#222;margin-left:6px}

.season{left:361px;top:375px;width:713px;height:220px;overflow:hidden}
.season-head{height:43px;background:linear-gradient(var(--orange-light),var(--orange));color:#fff;font-size:18px;padding:11px 0 0 24px}
.grid-table{left:0;top:43px;width:713px;height:177px}
.vline{position:absolute;top:0;bottom:0;width:1px;background:var(--line)}
.hline{position:absolute;left:0;right:0;height:1px;background:var(--line)}
.cell{position:absolute;font-size:13px;color:#333;text-align:center}
.comp{position:absolute;left:28px;font-size:14px;color:var(--purple-text)}

.career{left:126px;top:641px;width:532px;height:343px}
.panel-head{height:35px;background:var(--panel-head);border-bottom:1px solid #ddd;font-size:17px;padding:9px 0 0 17px;color:#333}
.chart{left:0;top:35px;width:530px;height:306px}

.history{left:669px;top:637px;width:406px;height:343px}
.history .panel-head{height:41px;position:relative;padding:0}
.hh{position:absolute;top:14px;font-size:17px;color:#333}
.hrow{position:absolute;left:0;width:404px;height:32.5px;border-bottom:1px solid var(--line);font-size:13px;color:#333}
.hrow span{position:absolute;top:9px}

.footer{left:0;top:1041px;width:1200px;height:57px;background:var(--footer);border-top:1px solid #ddd;font-size:12px;color:#555;padding:22px 0 0 128px}
</style>
</head>
<body>

<header class="abs header">
  <div class="abs brand-mark"></div>
  <div class="abs brand-name">Kickmark Data Systems</div>
  <div class="abs brand-tag">The dedicated specialists in soccer content services.</div>
  <label class="abs radio" style="left:568px"><i></i>Team</label>
  <label class="abs radio" style="left:648px"><i></i>Players</label>
  <div class="abs search">type your word</div>
  <div class="abs search-btn">
    <svg width="33" height="31" viewBox="0 0 33 31"><circle cx="15" cy="14" r="6" fill="none" stroke="#fff" stroke-width="2.4"/><line x1="19.5" y1="18.5" x2="24" y2="23" stroke="#fff" stroke-width="2.6" stroke-linecap="round"/></svg>
  </div>
  <div class="abs date">02 October 2014</div>
  <div class="abs today">Today's Matches</div>
</header>

<nav class="abs sidebar">
  <div class="side-head">Domestic Football</div>
  <div class="side-item"><svg class="flag" viewBox="0 0 21 13"><rect width="21" height="13" fill="#fff"/><rect x="9" width="3" height="13" fill="#d00"/><rect y="5" width="21" height="3" fill="#d00"/></svg>England</div>
  <div class="side-item"><svg class="flag" viewBox="0 0 21 13"><rect width="21" height="13" fill="#1a3d8f"/><path d="M0 0L21 13M21 0L0 13" stroke="#fff" stroke-width="2"/></svg>Scotland</div>
  <div class="side-item"><svg class="flag" viewBox="0 0 21 13"><rect width="21" height="13" fill="#c60b1e"/><rect y="3.3" width="21" height="6.4" fill="#ffc400"/></svg>Span</div>
  <div class="side-item"><svg class="flag" viewBox="0 0 21 13"><rect width="7" height="13" fill="#009246"/><rect x="7" width="7" height="13" fill="#fff"/><rect x="14" width="7" height="13" fill="#ce2b37"/></svg>Italy</div>
  <div class="side-item"><svg class="flag" viewBox="0 0 21 13"><rect width="21" height="4.4" fill="#000"/><rect y="4.3" width="21" height="4.4" fill="#d00"/><rect y="8.7" width="21" height="4.3" fill="#ffce00"/></svg>Germany</div>
  <div class="side-item"><svg class="flag" viewBox="0 0 21 13"><rect width="7" height="13" fill="#0055a4"/><rect x="7" width="7" height="13" fill="#fff"/><rect x="14" width="7" height="13" fill="#ef4135"/></svg>France</div>
  <div class="side-head">Continental Football</div>
  <div class="side-item plain">Champions Cup</div>
  <div class="side-item plain">Champions Cup Qual</div>
  <div class="side-item plain">Euro Trophy</div>
  <div class="side-item plain">Euro Cup</div>
  <div class="side-item plain">Euro Cup Qual</div>
</nav>

<section class="abs card profile">
  <div class="abs photo" role="img" aria-label="Player portrait photo"></div>
  <div class="abs p-name">Milan Vukasovic</div>
  <div class="abs p-club">Kingsbridge <svg class="flag" viewBox="0 0 21 13" style="width:24px;height:13px"><rect width="21" height="13" fill="#fff" stroke="#ddd"/><rect x="9" width="3" height="13" fill="#d00"/><rect y="5" width="21" height="3" fill="#d00"/></svg></div>
  <div class="abs facts" style="left:201px;top:96px">Date of Birth:<b>22/02/1984</b></div>
  <div class="abs facts" style="left:372px;top:96px">Age:<b>30</b></div>
  <div class="abs facts" style="left:476px;top:96px">Birth Place:<b>Sremska Mitroica, Serbia</b></div>
  <div class="abs facts" style="left:201px;top:123px;display:flex;align-items:center">Nationality:<b style="margin-left:17px">Serbia</b>
    <svg class="flag" viewBox="0 0 21 13" style="margin-left:6px"><rect width="21" height="4.4" fill="#c6363c"/><rect y="4.3" width="21" height="4.4" fill="#0c4076"/><rect y="8.7" width="21" height="4.3" fill="#fff" stroke="#ddd" stroke-width=".5"/></svg></div>
  <div class="abs facts" style="left:372px;top:123px">Height:<b>1.88m</b></div>
  <div class="abs facts" style="left:476px;top:123px">Weight:<b>86 kg/13st lbs</b></div>
  <div class="abs facts" style="left:201px;top:152px">Position:<b>Defender</b></div>
</section>

<section class="abs card season">
  <div class="season-head">This Season</div>
  <div class="abs grid-table">
    <div class="vline" style="left:165px"></div><div class="vline" style="left:257px"></div>
    <div class="vline" style="left:332px"></div><div class="vline" style="left:398px"></div>
    <div class="vline" style="left:470px"></div><div class="vline" style="left:545px"></div>
    <div class="vline" style="left:619px"></div>
    <div class="hline" style="top:52px"></div><div class="hline" style="top:84px"></div>

    <div class="comp" style="top:29px">Competition</div>
    <div class="cell" style="left:165px;width:92px;top:29px;text-align:left;padding-left:19px">Team</div>
    <svg class="abs" style="left:296px;top:24px" width="20" height="22" viewBox="0 0 20 22"><circle cx="10" cy="5" r="4.5" fill="var(--green)"/><path d="M1 21v-5a5 5 0 015-5h8a5 5 0 015 5v5z" fill="var(--green)"/></svg>
    <svg class="abs" style="left:358px;top:30px" width="16" height="12" viewBox="0 0 16 12"><path d="M2 6l4 4 8-8" fill="none" stroke="var(--orange)" stroke-width="2.6"/></svg>
    <svg class="abs" style="left:423px;top:24px" width="22" height="22" viewBox="0 0 22 22"><path d="M4 11a7 7 0 0112-5" fill="none" stroke="var(--green)" stroke-width="2.5"/><path d="M18 11a7 7 0 01-12 5" fill="none" stroke="var(--orange)" stroke-width="2.5"/><path d="M17 2v5h-5z" fill="var(--green)"/><path d="M5 20v-5h5z" fill="var(--orange)"/></svg>
    <svg class="abs" style="left:501px;top:28px" width="14" height="14" viewBox="0 0 14 14"><circle cx="7" cy="7" r="6" fill="#fff" stroke="#333" stroke-width="1.3"/><circle cx="7" cy="7" r="2.5" fill="#333"/></svg>
    <svg class="abs" style="left:575px;top:28px" width="15" height="15"><circle cx="7.5" cy="7.5" r="7" fill="#ffd000"/></svg>
    <svg class="abs" style="left:650px;top:28px" width="15" height="15"><circle cx="7.5" cy="7.5" r="7" fill="#ff6a00"/></svg>

    <div class="comp" style="top:63px">Premier Division</div>
    <div class="cell" style="left:165px;top:63px;padding-left:19px">Kingsbridge</div>
    <div class="cell" style="left:257px;width:75px;top:63px">06</div>
    <div class="cell" style="left:332px;width:66px;top:63px">06</div>
    <div class="cell" style="left:398px;width:72px;top:63px">-</div>
    <div class="cell" style="left:470px;width:75px;top:63px">02</div>
    <div class="cell" style="left:545px;width:74px;top:63px">01</div>
    <div class="cell" style="left:619px;width:76px;top:63px">-</div>

    <div class="comp" style="top:96px">Champions Cup</div>
    <div class="cell" style="left:165px;top:96px;padding-left:19px">Kingsbridge</div>
    <div class="cell" style="left:257px;width:75px;top:96px">02</div>
    <div class="cell" style="left:332px;width:66px;top:96px">02</div>
    <div class="cell" style="left:398px;width:72px;top:96px">-</div>
    <div class="cell" style="left:470px;width:75px;top:96px">-</div>
    <div class="cell" style="left:545px;width:74px;top:96px">01</div>
    <div class="cell" style="left:619px;width:76px;top:96px">-</div>
  </div>
</section>

<section class="abs card career">
  <div class="panel-head">Career</div>
  <svg class="abs chart" viewBox="0 0 574 332" preserveAspectRatio="none" font-family="Oxygen, sans-serif" font-size="13" fill="#333">
    <defs>
      <linearGradient id="purpleFill" x1="0" y1="0" x2="1" y2="1">
        <stop offset="0" stop-color="#6a1fb5"/><stop offset="1" stop-color="#9a5ad0"/>
      </linearGradient>
    </defs>
    <g stroke="#e3e3e3">
      <line x1="42" y1="20" x2="574" y2="20"/><line x1="42" y1="55" x2="574" y2="55"/>
      <line x1="42" y1="90" x2="574" y2="90"/><line x1="42" y1="125" x2="574" y2="125"/>
      <line x1="42" y1="160" x2="574" y2="160"/><line x1="42" y1="195" x2="574" y2="195"/>
      <line x1="42" y1="230" x2="574" y2="230"/><line x1="42" y1="265" x2="574" y2="265"/>
      <line x1="0" y1="289" x2="574" y2="289"/><line x1="42" y1="0" x2="42" y2="332"/>
    </g>
    <g text-anchor="middle">
      <text x="24" y="24">40</text><text x="24" y="59">35</text><text x="24" y="94">30</text>
      <text x="24" y="129">25</text><text x="24" y="164">20</text><text x="24" y="199">15</text>
      <text x="24" y="234">10</text><text x="21" y="269">5</text>
      <text x="69" y="310">2005</text><text x="126" y="310">2007</text><text x="183" y="310">2008</text>
      <text x="240" y="310">2009</text><text x="296" y="310">2010</text><text x="353" y="310">2011</text>
      <text x="409" y="310">2012</text><text x="466" y="310">2013</text><text x="523" y="310">2014</text>
    </g>
    <polygon points="42,92 132,123 152,289 42,289" fill="var(--green)"/>
    <polyline points="42,92 132,123 152,289" fill="none" stroke="var(--orange)" stroke-width="3"/>
    <polygon points="182,284 209,193 272,153 326,133 390,165 434,118 489,103 574,232 574,289 182,289" fill="url(#purpleFill)"/>
    <polyline points="182,284 209,193 272,153 326,133 390,165 434,118 489,103 574,232" fill="none" stroke="var(--orange)" stroke-width="3"/>
    <g fill="var(--orange-light)">
      <circle cx="132" cy="123" r="5"/><circle cx="182" cy="284" r="5"/><circle cx="209" cy="193" r="5"/>
      <circle cx="272" cy="153" r="5"/><circle cx="326" cy="133" r="5"/><circle cx="390" cy="165" r="5"/>
      <circle cx="434" cy="118" r="5"/><circle cx="489" cy="103" r="5"/>
    </g>
  </svg>
</section>

<section class="abs card history">
  <div class="panel-head">
    <span class="hh" style="left:28px">Season</span>
    <svg class="abs" style="left:115px;top:11px" width="20" height="22" viewBox="0 0 20 22"><circle cx="10" cy="5" r="4.5" fill="var(--orange)"/><path d="M1 21v-5a5 5 0 015-5h8a5 5 0 015 5v5z" fill="var(--orange)"/></svg>
    <svg class="abs" style="left:180px;top:9px" width="26" height="26" viewBox="0 0 26 26"><circle cx="13" cy="13" r="11.5" fill="#fff" stroke="var(--green)" stroke-width="2"/><polygon points="13,8 17.5,11 16,16.5 10,16.5 8.5,11" fill="var(--green)"/><path d="M13 2v6M22.5 9l-5 2M19 22l-3-5.5M7 22l3-5.5M3.5 9l5 2" stroke="var(--green)" stroke-width="1.6"/></svg>
    <span class="hh" style="left:240px">Team</span>
  </div>
  <div class="hrow" style="top:48px"><span style="left:29px">2014-2015</span><span style="left:121px">06</span><span style="left:189px">02</span><svg class="abs flag" style="left:243px;top:10px" viewBox="0 0 21 13"><rect width="21" height="13" fill="#fff"/><rect x="9" width="3" height="13" fill="#d00"/><rect y="5" width="21" height="3" fill="#d00"/></svg><span style="left:277px">Kingsbridge</span></div>
  <div class="hrow" style="top:80.5px"><span style="left:29px">2013-2014</span><span style="left:121px">36</span><span style="left:189px">03</span><svg class="abs flag" style="left:243px;top:10px" viewBox="0 0 21 13"><rect width="21" height="13" fill="#fff"/><rect x="9" width="3" height="13" fill="#d00"/><rect y="5" width="21" height="3" fill="#d00"/></svg><span style="left:277px">Kingsbridge</span></div>
  <div class="hrow" style="top:113px"><span style="left:29px">2012-2013</span><span style="left:121px">34</span><span style="left:189px">05</span><svg class="abs flag" style="left:243px;top:10px" viewBox="0 0 21 13"><rect width="21" height="13" fill="#fff"/><rect x="9" width="3" height="13" fill="#d00"/><rect y="5" width="21" height="3" fill="#d00"/></svg><span style="left:277px">Kingsbridge</span></div>
  <div class="hrow" style="top:145.5px"><span style="left:29px">2011-2012</span><span style="left:121px">29</span><span style="left:189px">03</span><svg class="abs flag" style="left:243px;top:10px" viewBox="0 0 21 13"><rect width="21" height="13" fill="#fff"/><rect x="9" width="3" height="13" fill="#d00"/><rect y="5" width="21" height="3" fill="#d00"/></svg><span style="left:277px">Kingsbridge</span></div>
  <div class="hrow" style="top:178px"><span style="left:29px">2010-2011</span><span style="left:121px">34</span><span style="left:189px">04</span><svg class="abs flag" style="left:243px;top:10px" viewBox="0 0 21 13"><rect width="21" height="13" fill="#fff"/><rect x="9" width="3" height="13" fill="#d00"/><rect y="5" width="21" height="3" fill="#d00"/></svg><span style="left:277px">Kingsbridge</span></div>
  <div class="hrow" style="top:210.5px"><span style="left:29px">2009-2010</span><span style="left:121px">28</span><span style="left:195px">-</span><svg class="abs flag" style="left:243px;top:10px" viewBox="0 0 21 13"><rect width="21" height="13" fill="#fff"/><rect x="9" width="3" height="13" fill="#d00"/><rect y="5" width="21" height="3" fill="#d00"/></svg><span style="left:277px">Kingsbridge</span></div>
  <div class="hrow" style="top:243px"><span style="left:29px">2008-2009</span><span style="left:121px">16</span><span style="left:195px">-</span><svg class="abs flag" style="left:243px;top:10px" viewBox="0 0 21 13"><rect width="21" height="13" fill="#fff"/><rect x="9" width="3" height="13" fill="#d00"/><rect y="5" width="21" height="3" fill="#d00"/></svg><span style="left:277px">Kingsbridge</span></div>
  <div class="hrow" style="top:275.5px"><span style="left:29px">2007</span><span style="left:121px">26</span><span style="left:189px">03</span><svg class="abs flag" style="left:243px;top:10px" viewBox="0 0 21 13"><rect width="21" height="4.4" fill="#e03030"/><rect y="4.3" width="21" height="4.4" fill="#2d4fb0"/><rect y="8.7" width="21" height="4.3" fill="#f0f0f0"/></svg><span style="left:277px">Dvina Sporting</span></div>
</section>

<footer class="abs footer">© 2014 Company Name.&nbsp; All right reserved.&nbsp; Term of Use</footer>

</body>
</html>
```